Varro's Electrical & Solar Corflute Signage Design

So my plan is to put this design onto a 600 by 400 corflute sign (this sign will be printed out and cable tied to a fence FYI). I would like to have the name and the icon stand out. I need Varro's Electrical & Solar to be big and clear and I would like to have my "S" icon faded behind "Varro's Electrical & Solar" in the background.

I want to have my Lic No. - Top left with my ABN directly underneath. (I Want two ticks infront of them like this)
✓ Lic No. 582164K
✓ ABN 41 276 519 683

I want to have written on it: ALL ASPECTS OF ELECTRICAL (please use cool fonts and nothing too plain)
I also want to have: YOUR LOCAL TRUSTED ELECTRICIAN but if it looks too dicky then just have "all aspects of electrical" and just "free quotes • fast service" somewhere.
Directly underneath (smaller but still clear): FREE QUOTES • FAST SERVICE

At the bottom, I need my phone number big and clear - 0438 617 905 I would like this on a banner meaning like a cool strip at the bottom. (Please make the strip/banner look cool and not boring. Maybe shade the colour or something)
I also want the Facebook & Instagram icons on there so people can look us up on facebook & Instagram (make them match the colour of my logo or you could try any other colour that works)
Thank you so much!!

Colors

Designer to choose colors to be used in the design.

Requirements
Should not have
• no different colours other then the colours on my logo and icon

```html
<!DOCTYPE html>
<html lang="en">
<head>
<meta charset="utf-8">
<title>Varro's Electrical &amp; Solar – Corflute Sign</title>
<link rel="stylesheet" href="https://fonts.googleapis.com/css2?family=Montserrat:wght@700;800&display=swap">
<style>
  :root {
    --green: #2bb04a;
    --green-light: #3dba52;
    --green-dark: #1e8f3a;
    --charcoal: #3a424b;
    --white: #ffffff;
  }
  html, body {
    margin: 0;
    padding: 0;
    width: 1200px;
    height: 841px;
    overflow: hidden;
    background: var(--white);
  }
  .sign {
    position: relative;
    width: 1200px;
    height: 841px;
    background: var(--white);
    font-family: "Montserrat", Arial, sans-serif;
    font-weight: 800;
    color: var(--charcoal);
  }
  .sign__frame {
    position: absolute;
    left: 27px;
    top: 25px;
    width: 1134px;
    height: 783px;
    border: 5px solid var(--green);
    border-radius: 40px;
    overflow: hidden;
  }
  .phone-banner {
    position: absolute;
    left: 0;
    right: 0;
    bottom: 0;
    height: 112px;
    background: linear-gradient(180deg, var(--green-light) 0%, var(--green) 55%, var(--green-dark) 100%);
    display: flex;
    align-items: center;
    justify-content: center;
  }
  .phone-banner__number {
    margin: 0;
    font-size: 92px;
    font-weight: 800;
    line-height: 1;
    color: var(--white);
    letter-spacing: 1px;
  }
  .brand-name {
    position: absolute;
    left: 0;
    right: 0;
    top: 96px;
    margin: 0;
    text-align: center;
    font-size: 60px;
    font-weight: 800;
    line-height: 1;
    color: var(--green);
  }
  .headline {
    position: absolute;
    left: 0;
    right: 0;
    margin: 0;
    text-align: center;
    font-weight: 800;
    line-height: 1;
    white-space: nowrap;
  }
  .headline--services {
    top: 268px;
    font-size: 68px;
    color: var(--green-light);
  }
  .headline--aspects {
    top: 352px;
    font-size: 68px;
    color: var(--charcoal);
  }
  .offer-band {
    position: absolute;
    left: 32px;
    top: 454px;
    width: 1134px;
    height: 103px;
    background: var(--green);
    display: flex;
    align-items: center;
    justify-content: center;
  }
  .offer-band__text {
    margin: 0;
    font-size: 66px;
    font-weight: 800;
    line-height: 1;
    color: var(--white);
    white-space: nowrap;
  }
  .credentials {
    position: absolute;
    left: 58px;
    top: 578px;
    margin: 0;
    padding: 0;
    list-style: none;
    font-size: 40px;
    font-weight: 800;
    line-height: 50px;
  }
  .credentials__item {
    display: flex;
    align-items: center;
    gap: 12px;
  }
  .credentials__tick { width: 30px; height: 30px; flex: none; }
  .credentials__label { color: var(--green); }
  .credentials__value { color: var(--charcoal); }
  .social {
    position: absolute;
    left: 837px;
    top: 585px;
    display: flex;
    gap: 15px;
  }
  .social__dot {
    width: 36px;
    height: 36px;
    border-radius: 50%;
    background: var(--charcoal);
  }
  .badge {
    position: absolute;
    left: 1020px;
    top: 572px;
    width: 114px;
    height: 114px;
  }
</style>
</head>
<body>
  <main class="sign">
    <div class="sign__frame">
      <div class="phone-banner">
        <p class="phone-banner__number">0438 617 905</p>
      </div>
    </div>

    <h1 class="brand-name">VARRO'S ELECTRICAL &amp; SOLAR</h1>

    <p class="headline headline--services">ELECTRICAL &amp; SOLAR</p>
    <p class="headline headline--aspects">ALL ASPECTS OF ELECTRICAL</p>

    <div class="offer-band">
      <p class="offer-band__text">FREE QUOTES &amp; FAST SERVICE</p>
    </div>

    <ul class="credentials">
      <li class="credentials__item">
        <svg class="credentials__tick" viewBox="0 0 30 30" aria-hidden="true"><path d="M4 16 L12 24 L26 7" fill="none" stroke="var(--green)" stroke-width="5" stroke-linecap="round" stroke-linejoin="round"/></svg>
        <span><span class="credentials__label">Lic No.</span> <span class="credentials__value">582164K</span></span>
      </li>
      <li class="credentials__item">
        <svg class="credentials__tick" viewBox="0 0 30 30" aria-hidden="true"><path d="M4 16 L12 24 L26 7" fill="none" stroke="var(--green)" stroke-width="5" stroke-linecap="round" stroke-linejoin="round"/></svg>
        <span class="credentials__value">ABN 41 276 519 683</span>
      </li>
    </ul>

    <div class="social" aria-label="Social media">
      <span class="social__dot"></span>
      <span class="social__dot"></span>
      <span class="social__dot"></span>
    </div>

    <svg class="badge" viewBox="0 0 114 114" role="img" aria-label="Varro's badge">
      <circle cx="57" cy="57" r="53" fill="none" stroke="var(--green)" stroke-width="5"/>
      <text x="57" y="64" text-anchor="middle" font-family="Montserrat, Arial, sans-serif" font-weight="800" font-size="18" fill="var(--green)">VARRO'S</text>
    </svg>
  </main>
</body>
</html>
```